Business card for a business coach / management consultant

My logo has been done and now I need a business card. Deliverable needs to be a PDF to give to the printer. I want it single sided as I want the back side blank.
I prefer a white card with modern simple professional design.
Details are:
Tobias Wrenfield
B.Sc. (hons) FRTB CP MEGOL
14 Calloway Rd
Kestrel Vale WA 6072
Australia
mobile 041 23 584 17
email tobias@corporatepathlane.com.au
chat tobiaswrenfield8
Small to medium size business owners
Business

```html
<!DOCTYPE html>
<html lang="en">
<head>
<meta charset="utf-8">
<title>Corporate Pathlane – Business Card</title>
<link rel="stylesheet" href="https://fonts.googleapis.com/css2?family=Arimo:wght@400;700&display=swap">
<style>
  :root {
    --backdrop: #ecebea;
    --card: #ffffff;
    --brand-blue: #2b4f93;
    --slate: #9a9ea3;
    --ink-soft: #4d6aa3;
  }
  * { margin: 0; padding: 0; box-sizing: border-box; }
  html, body {
    width: 1200px; height: 1000px; overflow: hidden;
    background: var(--backdrop);
    font-family: "Arimo", Arial, sans-serif;
  }
  .canvas { position: relative; width: 1200px; height: 1000px; }
  .business-card {
    position: absolute; left: 150px; top: 228px;
    width: 900px; height: 545px;
    background: var(--card);
    box-shadow: 0 6px 24px rgba(0,0,0,0.12);
    overflow: hidden;
  }
  .edge-band { position: absolute; left: 0; top: 0; width: 30px; height: 100%; }
  .edge-band__blue { height: 58%; background: var(--brand-blue); }
  .edge-band__grey { height: 42%; background: var(--slate); }

  .brand-lockup {
    position: absolute; right: 60px; top: 60px;
    display: flex; flex-direction: column; align-items: flex-end; gap: 22px;
  }
  .brand-lockup__dot {
    width: 150px; height: 150px; border-radius: 50%;
    background: var(--brand-blue);
  }
  .brand-lockup__name {
    font-weight: 700; font-size: 40px; color: var(--brand-blue);
    letter-spacing: -0.5px; white-space: nowrap;
  }

  .holder { position: absolute; left: 90px; top: 140px; }
  .holder__name {
    font-weight: 400; font-size: 46px; color: var(--brand-blue);
    letter-spacing: 1px; white-space: nowrap;
  }
  .holder__credentials {
    margin-top: 8px; font-size: 18px; color: var(--ink-soft);
    letter-spacing: 1.5px; white-space: nowrap;
  }

  .contact-list {
    position: absolute; left: 120px; top: 300px;
    list-style: none; font-size: 21px; color: var(--ink-soft);
  }
  .contact-list li {
    display: flex; align-items: flex-start; gap: 14px;
    margin-bottom: 16px; line-height: 1.35; white-space: nowrap;
  }
  .contact-list svg { flex: none; width: 24px; height: 24px; margin-top: 2px; fill: var(--brand-blue); }
</style>
</head>
<body>
<div class="canvas">
  <div class="business-card">
    <div class="edge-band">
      <div class="edge-band__blue"></div>
      <div class="edge-band__grey"></div>
    </div>

    <div class="brand-lockup">
      <div class="brand-lockup__dot"></div>
      <div class="brand-lockup__name">Corporate Pathlane</div>
    </div>

    <div class="holder">
      <h1 class="holder__name">Tobias Wrenfield</h1>
      <p class="holder__credentials">B.Sc. (hons) FRTB CP MEGOL</p>
    </div>

    <ul class="contact-list">
      <li>
        <svg viewBox="0 0 24 24" aria-hidden="true"><path d="M12 1a8 8 0 0 0-8 8c0 6 8 14 8 14s8-8 8-14a8 8 0 0 0-8-8zm0 11a3 3 0 1 1 0-6 3 3 0 0 1 0 6z"/></svg>
        <span>14 Calloway Rd<br>Kestrel Vale WA 6072 Australia</span>
      </li>
      <li>
        <svg viewBox="0 0 24 24" aria-hidden="true"><path d="M6.6 2.5l3 3.6-2 2.3a13 13 0 0 0 8 8l2.3-2 3.6 3-2.4 3.3C11.5 21 3 12.5 3.3 4.9z"/></svg>
        <span>041 23 584 17</span>
      </li>
      <li>
        <svg viewBox="0 0 24 24" aria-hidden="true"><path d="M2 5h20v14H2zm2 2v.5l8 5.5 8-5.5V7z"/></svg>
        <span>tobias@corporatepathlane.com.au</span>
      </li>
      <li>
        <svg viewBox="0 0 24 24" aria-hidden="true"><circle cx="12" cy="12" r="10"/></svg>
        <span>chat: tobiaswrenfield8</span>
      </li>
    </ul>
  </div>
</div>
</body>
</html>
```